Regional Showdown Flyer for Holiday Program

Need a one page flyer, can be back to front or one page, ensuring you can fit all information, colourful, aimed at a market of 8-13 year old boys and girls.
The flyer needs to be noticed, needs to have certain information on it and needs to be Autralian Rule Football orientated.
Have uploaded file so you can understand the style (not content), style of flyer I am looking at getting submitted.

Target Market(s)

8-13 year old boys and girls and their parents.

Requirements
Must have
• Regional Showdown Event
• Price for Regional Showdown Day will be $85
• Strictly Limited Places, only the best footballers should enter this challenge
• Inaugural event, be the first Regional Showdown Winner for your age!
• Do you love a challenge! Put yourself to the test!
• Are you up to it - Water Slide Goal Kicking Contest! The fastest kick in the West (tested by our very own speed gun)! Can you survive the Footy Titan Trail or Last One Standing Goal Kicking! These challenges are crazy are super fun!
• If you think you can deliver on the big stage then this is for YOU!
• All District age winners will receive prizes, awards and the adulation from all their peers!
• Year's 3-5 from 9am to 12pm
• Year's 6-8 from 1-4pm
• All challengers compete against their own age
• Lunch Provided
• Monday 16th April - Upper Tarrowby Regional Showdown Day at Tarrowby Oval
• Tuesday 17th April - North Tarrowby Regional Showdown Day at Kilmorna Reserve
• Wednesday 18th April - Yarlo Regional Showdown Day - Dunhaven Football Club
• Every Challenge Participant receives a District Football!
• Need to put all 3 District Football Logos on the bottom of the flyer, logos attached at bottom.
Nice to have
• Plenty of colour, if you can fit all information on one page that would be fine
Should not have
• Dull, boring, any footballs should be Aussie Rules footballs not NFL or soccer

```html
<!DOCTYPE html>
<html lang="en">
<head>
<meta charset="utf-8">
<title>Regional Showdown Event</title>
<link href="https://fonts.googleapis.com/css2?family=Yellowtail&family=Oswald:wght@600;700&family=Open+Sans:wght@400;700&family=Architects+Daughter&display=swap" rel="stylesheet">
<style>
:root{
  --red:#e3262b;
  --hot-red:#d81f3a;
  --magenta:#c8348e;
  --purple:#8e3f9c;
  --yellow:#f2c21b;
  --sun:#f6d736;
  --cyan:#4fc3e0;
  --blue:#1e9ad9;
  --navy:#1b2340;
  --ink:#222;
  --white:#fff;
  --cream:#fbf3c4;
}
*{margin:0;padding:0;box-sizing:border-box}
html,body{width:928px;height:1200px;overflow:hidden;background:var(--white)}
.flyer{position:relative;width:928px;height:1200px;overflow:hidden;background:var(--white);font-family:"Open Sans",sans-serif;color:var(--ink)}
.abs{position:absolute}
.paint-splash{left:0;top:0;width:928px;height:470px}
.football-art{left:22px;top:38px;width:330px;height:220px}
.title{font-family:"Yellowtail",cursive;font-weight:400;color:var(--white);line-height:1}
.title-line{position:absolute;white-space:nowrap;font-size:96px;transform:rotate(-12deg);transform-origin:left bottom}
.title-line.first{left:300px;top:95px}
.title-line.second{left:125px;top:185px}
.player-photo{left:590px;top:240px;width:338px;height:670px;z-index:1}
.price-splash{left:398px;top:215px;width:232px;height:240px;z-index:2}
.price{left:430px;top:275px;width:180px;text-align:center;transform:rotate(-10deg);font-family:"Oswald",sans-serif;font-weight:700;color:var(--white);text-transform:uppercase;font-size:20px;line-height:1.14;white-space:nowrap;z-index:3}
.price .amount{display:block;font-size:34px;margin-top:2px}
.limited{left:30px;top:362px;width:400px;text-align:center;font-weight:700;font-size:20px;line-height:1.3;text-transform:uppercase;color:var(--ink)}
.band{left:0;height:88px;display:flex;align-items:center;font-family:"Architects Daughter",cursive;font-size:20px;text-transform:uppercase;line-height:1.3;white-space:nowrap}
.band svg{position:absolute;left:0;top:0}
.band span{position:relative}
.band-yellow{top:474px;width:535px;padding-left:34px;color:var(--ink)}
.band-magenta{top:572px;width:470px;justify-content:center;text-align:center;color:var(--white);padding-right:20px}
.challenges{left:36px;top:686px;width:550px;font-size:15.5px;line-height:1.42;text-transform:uppercase}
.big-stage{left:36px;top:798px;width:540px;font-family:"Oswald",sans-serif;font-weight:600;font-size:27px;line-height:1.35;color:var(--hot-red);text-transform:uppercase;white-space:nowrap}
.footer-panel{left:0;top:880px;width:928px;height:320px;z-index:4}
.winners{left:0;top:946px;width:928px;text-align:center;font-size:14px;text-transform:uppercase;z-index:5}
.info{left:36px;top:1000px;width:720px;z-index:5}
.info p{font-weight:700;font-size:16px;text-transform:uppercase;margin-bottom:13px;white-space:nowrap}
.schedule{list-style:none;font-size:15px;line-height:1.45;margin:2px 0 14px;white-space:nowrap}
.schedule b{font-weight:700}
.clubs{left:770px;top:978px;width:124px;list-style:none;z-index:5}
.clubs li{display:flex;align-items:center;gap:6px;height:64px;margin-bottom:10px;background:var(--white);padding:0 6px;font-weight:700;font-size:13px;color:var(--navy);text-transform:uppercase;line-height:1.15}
.clubs li::before{content:"";width:12px;height:12px;border-radius:50%;background:var(--navy);flex:none}
</style>
</head>
<body>
<main class="flyer">
  <svg class="abs paint-splash" viewBox="0 0 928 470" role="img" aria-label="Colourful paint brush strokes in yellow, red, magenta and cyan">
    <defs>
      <linearGradient id="paint" x1="0" y1="1" x2="1" y2="0">
        <stop offset="0" stop-color="#4fc3e0"/>
        <stop offset=".25" stop-color="#8e3f9c"/>
        <stop offset=".5" stop-color="#e3262b"/>
        <stop offset=".75" stop-color="#c8348e"/>
        <stop offset="1" stop-color="#f2c21b"/>
      </linearGradient>
    </defs>
    <path fill="url(#paint)" d="M0 0H928V330C880 320 840 345 790 330C740 315 700 350 640 345C600 340 560 360 520 330C470 300 430 330 380 320C330 310 290 350 240 340C190 330 150 360 100 350C60 342 30 360 0 352Z"/>
  </svg>
  <svg class="abs football-art" viewBox="0 0 330 220" role="img" aria-label="Red Australian Rules football illustration">
    <ellipse cx="165" cy="110" rx="160" ry="100" fill="#e3262b"/>
  </svg>

  <h1 class="abs title"><span class="title-line first">Regional</span><span class="title-line second">Showdown Event</span></h1>

  <div class="abs player-photo" role="img" aria-label="Photo of a young player in a striped footy jumper holding a pink football" style="background:linear-gradient(180deg,#f1e2d0 0%,#2a3158 30%,#d6332f 55%,#f1b52c 70%,#1b2340 100%);"></div>

  <svg class="abs price-splash" viewBox="0 0 232 240" role="img" aria-label="Blue paint splash">
    <path fill="#1e9ad9" d="M116 6C140 30 170 10 188 36C210 62 232 90 218 126C206 160 226 196 190 214C160 232 130 224 104 236C74 226 40 230 22 200C4 172 20 140 8 110C0 78 26 52 52 36C74 22 94 0 116 6Z"/>
  </svg>
  <p class="abs price">Price for<br>Regional<br>Showdown Day<br>will be<span class="amount">$85</span></p>

  <p class="abs limited">Strictly limited places,<br>only the best footballers<br>should enter this challenge</p>

  <div class="abs band band-yellow">
    <svg width="535" height="88" viewBox="0 0 535 88"><path d="M0 0H535L490 88H0Z" fill="#f2c21b"/></svg>
    <span>Inaugural event, be the first Regional<br>Showdown winner for your age!</span>
  </div>
  <div class="abs band band-magenta">
    <svg width="470" height="88" viewBox="0 0 470 88"><path d="M0 0H470L430 88H0Z" fill="#c8348e"/></svg>
    <span>Do you love a challenge!<br>Put yourself to the test!</span>
  </div>

  <p class="abs challenges">Are you up to it - water slide goal kicking contest! The fastest kick in the west (tested by our very own speed gun)! Can you survive the Footy Titan Trail or Last One Standing goal kicking! These challenges are crazy are super fun!</p>

  <p class="abs big-stage">If you think you can deliver on<br>the big stage then this is for you!</p>

  <svg class="abs footer-panel" viewBox="0 0 928 320" aria-hidden="true">
    <defs>
      <linearGradient id="sunfade" x1="0" y1="0" x2="1" y2="0">
        <stop offset="0" stop-color="#f6d736"/>
        <stop offset=".6" stop-color="#fbf3c4"/>
        <stop offset="1" stop-color="#fffdf2"/>
      </linearGradient>
    </defs>
    <path fill="url(#sunfade)" d="M0 22L40 14L80 26L130 10L180 24L240 12L300 28L360 14L420 26L480 8L540 22L600 16L660 30L720 12L780 24L840 10L890 26L928 16V320H0Z"/>
  </svg>

  <p class="abs winners">All District age winners will receive prizes, awards and the adulation from all their peers!</p>

  <div class="abs info">
    <p>Year's 3-5 from 9am to 12pm &nbsp;|&nbsp; Year's 6-8 from 1-4pm</p>
    <p>All challengers compete against their own age, &nbsp;&nbsp;Lunch provided</p>
    <ul class="schedule">
      <li><b>Monday 16<sup>th</sup> April -</b> Upper Tarrowby Regional Showdown Day at Tarrowby Oval</li>
      <li><b>Tuesday 17<sup>th</sup> April -</b> North Tarrowby Regional Showdown Day at Kilmorna Reserve</li>
      <li><b>Wednesday 18<sup>th</sup> April -</b> Yarlo Regional Showdown Day - Dunhaven Football Club</li>
    </ul>
    <p>Every challenge participant receives a District football!</p>
  </div>

  <ul class="abs clubs">
    <li>Marlins District</li>
    <li>Yarlo District</li>
    <li>Hounds District</li>
  </ul>
</main>
</body>
</html>
```